Bright Oak Fitness Facility Business Cards

Business Card Design that incorporates the logo and tagline

Target Market(s)

Fitness, People Who Exercise

Contact Information for Business Card

2817 Mossgrove Bend Road
Tavares, Florida 32190
Phone: 352-555-Jump (5867)
www.brightoakfitness.example
info@brightoakfitness.example

Requirements
Must have
• Logo, Address, Website, email and tagline "More Than A Gym". Colors should be red/black/grey/white

```html
<!DOCTYPE html>
<html lang="en">
<head>
<meta charset="utf-8">
<title>Bright Oak Fitness Business Cards</title>
<link rel="stylesheet" href="https://fonts.googleapis.com/css2?family=Ubuntu:wght@400;500&display=swap">
<style>
  :root {
    --bg: #ebebed;
    --white: #ffffff;
    --red: #f50a0a;
    --red-text: #e3201b;
    --black: #0b0b0b;
    --icon-dark: #141515;
    --icon-pink: #f98b85;
    --ink: #111111;
  }
  * { box-sizing: border-box; margin: 0; padding: 0; }
  html, body { width: 1200px; height: 1200px; overflow: hidden; background: var(--bg); }
  body { position: relative; font-family: "Ubuntu", sans-serif; }

  .card {
    position: absolute;
    width: 546px;
    height: 956px;
    display: flex;
    flex-direction: column;
    background: var(--white);
  }
  .card--front { left: 32px; top: 38px; }
  .card--back  { left: 624px; top: 200px; }

  .brand {
    height: 269px;
    display: flex;
    align-items: center;
    justify-content: center;
    gap: 14px;
    background: var(--white);
  }
  .brand__dot {
    width: 34px; height: 34px;
    border-radius: 50%;
    background: var(--red);
  }
  .brand__name {
    font-size: 42px;
    font-weight: 500;
    color: var(--red);
  }

  .band {
    height: 137px;
    display: flex;
    align-items: center;
    justify-content: center;
    text-align: center;
  }
  .band--red { background: var(--red); }
  .band--black { background: var(--black); }

  .address {
    font-size: 37px;
    line-height: 1.4;
    letter-spacing: 0.5px;
    color: var(--ink);
  }
  .tagline {
    font-size: 47px;
    letter-spacing: 1px;
    color: var(--ink);
  }

  .contact {
    justify-content: flex-start;
    text-align: left;
  }
  .contact__icon {
    width: 146px;
    height: 100%;
    display: flex;
    align-items: center;
    justify-content: center;
    flex-shrink: 0;
  }
  .contact__icon--dark { background: var(--icon-dark); }
  .contact__icon--pink { background: var(--icon-pink); }
  .contact__icon svg { width: 80px; height: 80px; }
  .contact__text {
    padding-left: 6px;
    font-size: 23px;
    letter-spacing: 0.6px;
    white-space: nowrap;
  }
  .band--black .contact__text { color: var(--red-text); }
  .band--red .contact__text { color: var(--ink); }
</style>
</head>
<body>

<svg width="0" height="0" style="position:absolute" aria-hidden="true">
  <defs>
    <symbol id="icon-phone" viewBox="0 0 80 80">
      <path d="M14 10 L26 6 L34 24 L26 30 Q32 44 46 52 L52 44 L70 52 L66 64 Q60 74 48 70 Q20 58 8 28 Q6 16 14 10 Z" fill="#f50a0a"/>
      <path d="M46 14 Q62 18 66 34" stroke="#f50a0a" stroke-width="5" fill="none" stroke-linecap="round"/>
      <path d="M48 2 Q74 6 78 32" stroke="#f50a0a" stroke-width="5" fill="none" stroke-linecap="round"/>
    </symbol>
    <symbol id="icon-web" viewBox="0 0 80 80">
      <circle cx="40" cy="40" r="36" fill="none" stroke="#111" stroke-width="6"/>
      <ellipse cx="40" cy="40" rx="15" ry="36" fill="none" stroke="#111" stroke-width="5"/>
      <line x1="10" y1="20" x2="70" y2="20" stroke="#111" stroke-width="5"/>
      <line x1="10" y1="60" x2="70" y2="60" stroke="#111" stroke-width="5"/>
      <rect x="0" y="30" width="80" height="20" fill="#f98b85"/>
      <text x="40" y="47" text-anchor="middle" font-family="Ubuntu, sans-serif" font-weight="500" font-size="20" fill="#111">WWW</text>
    </symbol>
    <symbol id="icon-mail" viewBox="0 0 80 80">
      <rect x="4" y="14" width="72" height="54" fill="none" stroke="#f50a0a" stroke-width="7"/>
      <path d="M8 20 L40 48 L72 20" fill="none" stroke="#f50a0a" stroke-width="7"/>
    </symbol>
  </defs>
</svg>

<article class="card card--front">
  <header class="brand">
    <span class="brand__dot"></span>
    <span class="brand__name">Bright Oak Fitness</span>
  </header>
  <section class="band band--red">
    <p class="address">2817 Mossgrove Bend Road<br>Tavares, Florida 32190</p>
  </section>
  <section class="band band--black contact">
    <div class="contact__icon contact__icon--dark"><svg><use href="#icon-phone"/></svg></div>
    <p class="contact__text">352-555-Jump (5867)</p>
  </section>
  <section class="band band--red contact">
    <div class="contact__icon contact__icon--pink"><svg><use href="#icon-web"/></svg></div>
    <p class="contact__text">www.brightoakfitness.example</p>
  </section>
  <section class="band band--black contact">
    <div class="contact__icon contact__icon--dark"><svg><use href="#icon-mail"/></svg></div>
    <p class="contact__text">info@brightoakfitness.example</p>
  </section>
  <section class="band band--red">
    <p class="tagline">"More Than A Gym"</p>
  </section>
</article>

<article class="card card--back">
  <header class="brand">
    <span class="brand__dot"></span>
    <span class="brand__name">Bright Oak Fitness</span>
  </header>
  <section class="band band--red">
    <p class="tagline">"More Than A Gym"</p>
  </section>
  <section class="band band--black contact">
    <div class="contact__icon contact__icon--dark"><svg><use href="#icon-phone"/></svg></div>
    <p class="contact__text">352-555-Jump (5867)</p>
  </section>
  <section class="band band--red contact">
    <div class="contact__icon contact__icon--pink"><svg><use href="#icon-web"/></svg></div>
    <p class="contact__text">www.brightoakfitness.example</p>
  </section>
  <section class="band band--black contact">
    <div class="contact__icon contact__icon--dark"><svg><use href="#icon-mail"/></svg></div>
    <p class="contact__text">info@brightoakfitness.example</p>
  </section>
  <section class="band band--red">
    <p class="address">2817 Mossgrove Bend Road<br>Tavares, Florida 32190</p>
  </section>
</article>

</body>
</html>
```